Crestfield Automotive Business Card

Automotive repair , all makes including Asian and European Imports. QMR Certified (Logo),Chatterbook (logo), Pingly+ (logo)

Industry/Entity Type

Automotive

Contact Information for Business Card

Crestfield Automotive, Ray Hobart Owner, 3817 Larch Ave. Alderbrook, Qz 58402. Website crestfieldautomotive.example. (555) 641-0938

```html
<!DOCTYPE html>
<html lang="en">
<head>
<meta charset="utf-8">
<title>Crestfield Automotive – Business Card</title>
<link rel="stylesheet" href="https://fonts.googleapis.com/css2?family=Oswald:wght@600&family=Roboto:wght@400;700&display=swap">
<style>
  :root {
    --backdrop: #3a3a3c;
    --card-white: #ffffff;
    --engine-light: #e9eaec;
    --engine-mid: #cfd1d4;
    --brand-blue: #1d3f9c;
    --accent-red: #d0222e;
    --ink: #1e1e1e;
    --ink-soft: #333333;
    --social-blue: #3b5998;
  }
  * { box-sizing: border-box; margin: 0; padding: 0; }
  html, body {
    width: 1200px; height: 852px; overflow: hidden;
    background: var(--backdrop);
  }
  .canvas { position: relative; width: 1200px; height: 852px; }

  .card {
    position: absolute;
    width: 560px; height: 320px;
    border-radius: 26px;
    overflow: hidden;
    background: var(--card-white);
    box-shadow: 0 14px 30px rgba(0,0,0,.35);
  }
  .card--front { left: 60px; top: 80px; }
  .card--back  { left: 580px; top: 452px; }

  .engine-photo {
    position: absolute; inset: 0;
    background: radial-gradient(ellipse at 45% 45%, var(--engine-light) 0%, var(--engine-mid) 70%, #c2c4c8 100%);
  }
  .engine-veil { position: absolute; inset: 0; background: rgba(255,255,255,.45); }

  .brand-name {
    font-family: "Oswald", sans-serif;
    font-weight: 600;
    color: var(--brand-blue);
    text-transform: uppercase;
    line-height: 1.02;
    letter-spacing: .5px;
  }
  .card--front .brand-name {
    position: absolute; left: 0; right: 0; top: 112px;
    text-align: center; font-size: 44px;
  }
  .card--back .brand-name {
    position: absolute; left: 44px; top: 118px;
    font-size: 34px;
  }

  .contact {
    position: absolute; left: 300px; top: 60px; right: 20px;
    font-family: "Roboto", sans-serif;
    color: var(--ink-soft);
  }
  .contact__name { font-weight: 700; font-size: 19px; color: var(--ink); }
  .contact__role { font-size: 11px; color: var(--accent-red); margin-top: 3px; }
  .contact__list { list-style: none; margin-top: 34px; }
  .contact__item {
    display: flex; align-items: center; gap: 8px;
    font-size: 12px; margin-bottom: 7px; white-space: nowrap;
  }
  .contact__item svg { width: 11px; height: 11px; fill: var(--accent-red); flex: none; }

  .social { display: flex; gap: 14px; margin-top: 18px; padding-left: 20px; font-family: "Roboto", sans-serif; font-size: 10px; color: var(--ink-soft); }
  .social__item { display: flex; align-items: center; gap: 5px; }
  .social__dot { width: 12px; height: 12px; border-radius: 50%; }
  .social__dot--chat { background: var(--social-blue); }
  .social__dot--ping { background: var(--accent-red); }
</style>
</head>
<body>
<main class="canvas">
  <section class="card card--front">
    <div class="engine-photo" role="img" aria-label="Faded close-up photo of a car engine bay with hoses and wiring"></div>
    <div class="engine-veil"></div>
    <p class="brand-name">Crestfield<br>Automotive</p>
  </section>

  <section class="card card--back">
    <p class="brand-name">Crestfield<br>Automotive</p>
    <div class="contact">
      <p class="contact__name">Ray Hobart</p>
      <p class="contact__role">Owner</p>
      <ul class="contact__list">
        <li class="contact__item">
          <svg viewBox="0 0 24 24" aria-hidden="true"><path d="M6.6 10.8a15 15 0 0 0 6.6 6.6l2.2-2.2a1 1 0 0 1 1-.25 11.4 11.4 0 0 0 3.6.57 1 1 0 0 1 1 1V20a1 1 0 0 1-1 1A17 17 0 0 1 3 4a1 1 0 0 1 1-1h3.5a1 1 0 0 1 1 1c0 1.25.2 2.45.57 3.570a1 1 0 0 1-.25 1z"/></svg>
          (555) 641-0938
        </li>
        <li class="contact__item">
          <svg viewBox="0 0 24 24" aria-hidden="true"><path d="M12 2a10 10 0 1 0 0 20 10 10 0 0 0 0-20zm6.9 6h-2.9a15.7 15.7 0 0 0-1.4-3.6A8 8 0 0 1 18.9 8zM12 4c.8 1.2 1.5 2.5 1.9 4h-3.8c.4-1.4 1.1-2.8 1.9-4zM4.3 14a8.2 8.2 0 0 1 0-4h3.4a16.5 16.5 0 0 0 0 4zm.8 2h2.9c.3 1.3.8 2.5 1.4 3.6A8 8 0 0 1 5.1 16zM8 8H5.1a8 8 0 0 1 4.3-3.6C8.8 5.5 8.3 6.7 8 8zm4 12c-.8-1.2-1.5-2.5-1.9-4h3.8c-.4 1.4-1.1 2.8-1.9 4zm2.3-6H9.7a14.7 14.7 0 0 1 0-4h4.6a14.7 14.7 0 0 1 0 4zm.3 5.6c.6-1.1 1.1-2.3 1.4-3.6h2.9a8 8 0 0 1-4.3 3.6zm1.7-5.6a16.5 16.5 0 0 0 0-4h3.4a8.2 8.2 0 0 1 0 4z"/></svg>
          www.crestfieldautomotive.example
        </li>
        <li class="contact__item">
          <svg viewBox="0 0 24 24" aria-hidden="true"><path d="M12 2a7 7 0 0 0-7 7c0 5.2 7 13 7 13s7-7.800 7-13a7 7 0 0 0-7-7zm0 9.5A2.5 2.5 0 1 1 12 6.5a2.5 2.5 0 0 1 0 5z"/></svg>
          3817 Larch Ave. Alderbrook, Qz 58402
        </li>
      </ul>
      <div class="social">
        <span class="social__item"><span class="social__dot social__dot--chat"></span>Chatterbook</span>
        <span class="social__item"><span class="social__dot social__dot--ping"></span>Pingly+</span>
      </div>
    </div>
  </section>
</main>
</body>
</html>
```